Hair Extension Packaging

Update 2/16 - please keep submissions coming, I have no front runners yet. Thanks.

I need some new packaging designed for hair extensions. I have enclose pictures of what other companies packaging looks like and a few pictures of some inspiration. I am looking for a packaging that will appeal to a 20's-30's year old demographic and I like things along the lines of glamor/lace/vintage/boudoir/damask inspired. I am going to leave colors up to your creativity for the sample artwork and ask for changes if needed. Id like the design to be a standout but not loud.

The working name for this hair is "Velvetta"
Additional Text that I would like on the packaging "100% Premium Virgin Remy Human Hair"

Please keep in mind that the background of the packaging will have many different colors laying over it so be mindful of what the color you chose can effect the hair color in the packaging - no red or orange which can make the hair appear very warm and clash with ashy colors.

Working dimensions for the sample are 22" long, 3" wide.

****Once I decide on the front of the packaging I will also need the back designed which will consist of similar design as the front but with hair care instructions printed on it.***** This finished product must include front and back artwork, open Photoshop files, and additional bleed room for printing. I don't want to waste anyone's time so once I get a front design I like I will work with that artist to create the back.

Please message me with any questions.
Updates

Project Deadline Extended
Reason: Finalizing final choices. Thanks for your submissions!

Target Market(s)

Women in there 20"s - 30's. High fashion, luxurious, glamour

Industry/Entity Type

Hair

Font styles to use
Serif
Script

Requirements
Must have
• Id love the product name to be in script and then mixed with regular font (see the makeup logo example I enclosed)
Should not have
• Should not be masculine. Forget the blue and green colors

```html
<!DOCTYPE html>
<html lang="en">
<head>
<meta charset="utf-8">
<title>Velvetta – Hair Extension Packaging</title>
<link rel="stylesheet" href="https://fonts.googleapis.com/css2?family=Cormorant+Garamond:wght@500;600&display=swap">
<style>
  :root {
    --backdrop: #3b2a1f;
    --cocoa-deep: #2a1810;
    --cocoa: #4a2c1d;
    --cocoa-glow: #6a3f28;
    --gold: #e6b256;
    --parchment-light: #f3cd7c;
    --parchment: #e6b35e;
    --parchment-edge: #c98e3c;
    --frame-line: #e8dccb;
    --tagline: #8a6c58;
  }
  * { margin: 0; padding: 0; box-sizing: border-box; }
  html, body { width: 1200px; height: 800px; overflow: hidden; }
  body {
    background: var(--backdrop);
    font-family: "Cormorant Garamond", Georgia, serif;
    position: relative;
  }
  .package { position: absolute; overflow: hidden; box-shadow: 0 6px 24px rgba(0,0,0,.45); }
  .package--strip { left: 351px; top: 50px; width: 96px; height: 700px; }
  .package--detail { left: 586px; top: 152px; width: 450px; height: 648px; }
  .package-art { position: absolute; inset: 0; width: 100%; height: 100%; }
  .portrait-area { position: absolute; }
  .package--strip .portrait-area { left: 28px; top: 6px; width: 40px; height: 34px; }
  .package--detail .portrait-area { left: 144px; top: 42px; width: 200px; height: 210px; }
  .brand-name {
    position: absolute; left: 0; right: 0; text-align: center;
    color: var(--gold); font-weight: 600; line-height: 1;
  }
  .package--strip .brand-name { top: 44px; font-size: 21px; letter-spacing: .5px; }
  .package--detail .brand-name { top: 232px; font-size: 104px; letter-spacing: 2px; }
  .tagline-small {
    position: absolute; left: 4px; right: 4px; top: 90px; text-align: center;
    font-size: 3.4px; letter-spacing: .3px; text-transform: uppercase; color: var(--tagline);
  }
</style>
</head>
<body>

<section class="package package--strip" aria-label="Velvetta package, full length">
  <svg class="package-art" viewBox="0 0 96 700" preserveAspectRatio="none" aria-hidden="true">
    <defs>
      <radialGradient id="stripCocoa" cx="50%" cy="40%" r="70%">
        <stop offset="0" stop-color="var(--cocoa-glow)"/>
        <stop offset="1" stop-color="var(--cocoa-deep)"/>
      </radialGradient>
      <linearGradient id="stripParchment" x1="0" y1="0" x2="0" y2="1">
        <stop offset="0" stop-color="var(--parchment-light)"/>
        <stop offset=".6" stop-color="var(--parchment)"/>
        <stop offset="1" stop-color="var(--parchment-edge)"/>
      </linearGradient>
    </defs>
    <rect width="96" height="700" fill="url(#stripCocoa)"/>
    <rect x="3" y="3" width="90" height="98" fill="none" stroke="var(--frame-line)" stroke-width=".5"/>
    <path d="M0 112 Q48 94 96 112 V700 H0 Z" fill="url(#stripParchment)"/>
  </svg>
  <div class="portrait-area" role="img" aria-label="Vintage sepia engraving of a figure"
       style="background: radial-gradient(ellipse at center, rgba(40,22,14,.8), rgba(40,22,14,0) 70%);"></div>
  <div class="brand-name">Velvetta</div>
  <div class="tagline-small">100% Premium Virgin Remy Human Hair</div>
</section>

<section class="package package--detail" aria-label="Velvetta package, top detail">
  <svg class="package-art" viewBox="0 0 450 648" aria-hidden="true">
    <defs>
      <radialGradient id="detailCocoa" cx="48%" cy="38%" r="65%">
        <stop offset="0" stop-color="var(--cocoa-glow)"/>
        <stop offset=".55" stop-color="var(--cocoa)"/>
        <stop offset="1" stop-color="var(--cocoa-deep)"/>
      </radialGradient>
      <radialGradient id="detailParchment" cx="50%" cy="30%" r="80%">
        <stop offset="0" stop-color="var(--parchment-light)"/>
        <stop offset=".7" stop-color="var(--parchment)"/>
        <stop offset="1" stop-color="var(--parchment-edge)"/>
      </radialGradient>
      <path id="taglineArc" d="M36 456 Q225 430 414 456"/>
    </defs>
    <rect width="450" height="648" fill="url(#detailCocoa)"/>
    <path d="M18 19 H432 V482 Q225 430 18 482 Z" fill="none" stroke="var(--frame-line)" stroke-width="1.5"/>
    <path d="M0 512 Q225 440 450 512 V648 H0 Z" fill="url(#detailParchment)"/>
    <text font-family="Cormorant Garamond, Georgia, serif" font-size="15.5" letter-spacing="1" fill="var(--tagline)">
      <textPath href="#taglineArc" startOffset="50%" text-anchor="middle">100% PREMIUM VIRGIN REMY HUMAN HAIR</textPath>
    </text>
  </svg>
  <div class="portrait-area" role="img" aria-label="Vintage sepia engraving of a figure"
       style="background: radial-gradient(ellipse at 55% 45%, rgba(36,20,12,.75), rgba(36,20,12,0) 70%);"></div>
  <div class="brand-name">Velvetta</div>
</section>

</body>
</html>
```